Chimney Service company needs new business card design

We need a updated business card with our new logo added. We provide a full range of chimney services throughout Vermont and New Hampshire. The business card will be one sided and color. Attached is our current business card another document showing all the information we would like on the card.
We dont like a lot of flashy colors.... here is a link to our website to get an idea of our branding www.flueguardianvt.example

Target Market(s)

homeowners

Industry/Entity Type

Business

Contact Information for Business Card

See attached sheet for content.

Font styles to use
Serif
Sans Serif

Requirements
Must have
• all information provided on separate sheet
Should not have
• Additional information that may clogg up design

```html
<!DOCTYPE html>
<html lang="en">
<head>
<meta charset="utf-8">
<title>Flue Guardian — Business Card</title>
<link href="https://fonts.googleapis.com/css2?family=Cinzel:wght@400;700&family=Mulish:ital,wght@0,400;1,400&display=swap" rel="stylesheet">
<style>
  :root {
    --backdrop: #1c1c1c;
    --card-white: #ffffff;
    --card-dark: #323232;
    --ink: #2a2a2a;
    --brand-red: #a3161a;
    --logo-ink: #333333;
    --light: #ffffff;
  }
  * { margin: 0; padding: 0; box-sizing: border-box; }
  html, body { width: 1200px; height: 897px; overflow: hidden; background: var(--backdrop); }
  body { position: relative; font-family: "Mulish", sans-serif; color: var(--ink); }

  .card {
    position: absolute;
    left: 303px;
    width: 594px;
    height: 338px;
    border-radius: 19px;
  }
  .card--front { top: 92px; background: var(--card-white); }
  .card--back { top: 470px; background: var(--card-dark); }

  .brand-mark {
    position: absolute;
    left: 109px; top: 63px;
    width: 91px; height: 91px;
    border: 6px solid var(--logo-ink);
  }
  .brand-name {
    position: absolute;
    left: 0; width: 308px; top: 164px;
    text-align: center;
    font-family: "Cinzel", serif;
    font-size: 27px;
    letter-spacing: 0.5px;
    color: var(--logo-ink);
  }

  .service-area {
    position: absolute;
    left: 0; width: 308px; top: 260px;
    text-align: center;
  }
  .service-area__region {
    font-family: "Cinzel", serif;
    font-size: 14.5px;
    color: var(--ink);
    line-height: 19px;
  }
  .service-area__since {
    font-style: italic;
    font-size: 14px;
    color: var(--brand-red);
    line-height: 19px;
  }

  .contact {
    position: absolute;
    left: 331px; top: 53px;
    list-style: none;
  }
  .contact li {
    display: flex; align-items: center;
    height: 19.5px;
    font-size: 13.5px;
    letter-spacing: 0.2px;
  }
  .contact svg { width: 11px; height: 11px; margin-right: 12px; fill: var(--brand-red); }

  .services {
    position: absolute;
    left: 331px; top: 126px;
  }
  .services__title {
    font-family: "Cinzel", serif;
    font-weight: 700;
    font-size: 17.5px;
    color: var(--brand-red);
    line-height: 22px;
    margin-bottom: 1px;
  }
  .services__list { list-style: none; }
  .services__list li { font-size: 13.5px; line-height: 19.2px; }

  .promise {
    position: absolute;
    left: 331px; top: 260px;
    font-family: "Cinzel", serif;
    font-size: 14px;
    line-height: 19px;
    color: var(--brand-red);
  }

  .back-lockup {
    position: absolute;
    left: 0; right: 0; top: 132px;
    display: flex; align-items: center; justify-content: center;
    gap: 14px;
  }
  .back-lockup__mark { width: 68px; height: 72px; border: 5px solid var(--light); }
  .back-lockup__name {
    font-family: "Cinzel", serif;
    font-size: 38px;
    color: var(--light);
    letter-spacing: 0.5px;
  }
</style>
</head>
<body>
  <section class="card card--front">
    <div class="brand-mark"></div>
    <div class="brand-name">FLUE GUARDIAN</div>

    <div class="service-area">
      <p class="service-area__region">SERVING VT AND NEW HAMPSHIRE</p>
      <p class="service-area__since">since 1989</p>
    </div>

    <ul class="contact">
      <li>
        <svg viewBox="0 0 24 24"><path d="M6.6 10.8a15 15 0 0 0 6.6 6.6l2.2-2.2c.3-.3.7-.4 1-.2 1.1.4 2.3.6 3.6.6.6 0 1 .4 1 1V20c0 .6-.4 1-1 1A17 17 0 0 1 3 4c0-.6.4-1 1-1h3.5c.6 0 1 .4 1 1 0 1.3.2 2.5.6 3.6.1.3 0 .7-.2 1z"/></svg>
        802-555-0147
      </li>
      <li>
        <svg viewBox="0 0 24 24"><path d="M2 5h20v14H2z M2 5l10 8 10-8" fill="var(--brand-red)" stroke="#fff" stroke-width="1.5"/></svg>
        info@flueguardianvt.example
      </li>
      <li>
        <svg viewBox="0 0 24 24"><circle cx="12" cy="12" r="9.5" fill="none" stroke="var(--brand-red)" stroke-width="2"/><ellipse cx="12" cy="12" rx="4" ry="9.5" fill="none" stroke="var(--brand-red)" stroke-width="2"/><path d="M2.5 12h19M4 7h16M4 17h16" stroke="var(--brand-red)" stroke-width="2"/></svg>
        www.flueguardianvt.example
      </li>
    </ul>

    <div class="services">
      <h2 class="services__title">SERVICES WE PROVIDE</h2>
      <ul class="services__list">
        <li>Full Masonry Services</li>
        <li>Historic chimney restoration</li>
        <li>Stainless steel liners</li>
        <li>New Chimney installations</li>
        <li>QHTA Certified Chimney sweeps</li>
      </ul>
    </div>

    <div class="promise">
      <p>Fully Insured–Free Estimates</p>
      <p>&nbsp;Family Owned and Operated</p>
    </div>
  </section>

  <section class="card card--back">
    <div class="back-lockup">
      <div class="back-lockup__mark"></div>
      <div class="back-lockup__name">FLUE GUARDIAN</div>
    </div>
  </section>
</body>
</html>
```